BrightHarbor logo and website profile

BrightHarbor is a newly started business angel network investing in entrepreneurs and start-ups. We need a smart looking logo and website design (based on Wordpress).
The aim of the site is to attract 2 customer segments;
1) Entrepreneurs and start-ups looking for investors
2) Investors/ business angels looking to become part of a larger network of investors for better access to investments
A successful conversion on the website would be for the entrepreneur or investor sending us an e-mail to submit their investment proposal, inquire about our services or ask to join the network of investors.
The website should focus on presenting Bright Harbor and our offerings towards the 2 customer segments. This is NOT a platform like e.g. finchly.co.
Sites we like;
http://demo.pelmora.net/themes/orchid/agency/
http://www.tarnwickadvisory.no (it's a bit bleak - needs a little more color)
Target Market(s)
Two target markets; 1) entrepreneurs looking for investors 2) business angels looking for investment opportunities
Industry/Entity Type
Investment
Requirements
Must have
- The keywords we want associated with our brand are;
Innovation – Integrity – Knowledgeable – Growth – Entrepreneurship
Logodesign (symbol and smart presentation of the company name - bright harbor, both with and without .com)
Wordpress design, pages we need:
- landing page with clear CTA for entrepreneurs and clear CTA for investors
- Portfolio overview of investments made
- General page for our approach, services etc
- Contact us page
- Favicon
- News
- Header/footer information
Other functionality we need;
- Social media integration
The design must support mobile and iPads as well.
We like: less is more :)

```html
<!DOCTYPE html>
<html lang="en">
<head>
<meta charset="utf-8">
<title>Bright Harbor</title>
<link href="https://fonts.googleapis.com/css2?family=Oswald:wght@300;400;500&family=Titillium+Web:ital,wght@1,700&display=swap" rel="stylesheet">
<style>
:root{
  --red:#d0141f;
  --ink:#1a1a1a;
  --text:#444;
  --muted:#666;
  --black:#000;
  --band:#f4f4f4;
  --panel:#ebebeb;
  --footer-copy:#cfcfcf;
}
*{margin:0;padding:0;box-sizing:border-box}
html,body{width:784px;height:1200px;overflow:hidden;background:#fff;font-family:Arial,Helvetica,sans-serif;color:var(--text)}
.page{position:relative;width:784px;height:1200px}
.header{position:absolute;left:0;top:0;width:784px;height:51px;background:#fff}
.brand{position:absolute;left:10px;top:10px;display:flex;align-items:center;gap:6px;font-family:'Titillium Web',sans-serif;font-style:italic;font-weight:700;font-size:22px;color:var(--red);letter-spacing:.5px}
.brand-mark{width:14px;height:14px;background:var(--ink)}
.callus{position:absolute;right:12px;top:18px;font-family:Oswald,sans-serif;font-size:10px;font-weight:500;color:#333}
.callus span{font-weight:300;font-size:19px;color:#666}
.nav{position:absolute;left:0;top:51px;width:784px;height:46px;background:var(--black)}
.nav a{position:absolute;top:15px;color:#fff;text-decoration:none;font-size:11px;font-style:italic}
.hero{position:absolute;left:0;top:97px;width:784px;height:330px;background:var(--band)}
.values{position:absolute;left:0;top:427px;width:784px;height:100px;background:var(--band)}
.value{position:absolute;top:26px;width:150px;margin-left:-75px;text-align:center;color:var(--red);font-size:18px}
.value svg{display:block;margin:0 auto 8px;height:26px}
.audiences{position:absolute;left:0;top:527px;width:784px;height:611px;background:var(--panel)}
.audience{position:absolute;top:42px;width:300px}
.audience h2{font-family:Oswald,sans-serif;font-weight:500;font-size:21px;color:#555;letter-spacing:-.3px;line-height:1}
.audience .sub{font-family:Oswald,sans-serif;font-weight:400;font-size:11px;color:#777;text-align:right;margin-top:2px}
.audience p{font-size:10px;line-height:12px;color:#555;margin-top:16px;width:285px}
.cta{display:flex;align-items:center;gap:8px;margin-top:22px;font-size:8.5px;line-height:11px;color:var(--ink)}
.portfolio-title{position:absolute;left:0;top:230px;width:784px;text-align:center;font-family:Oswald,sans-serif;font-weight:300;font-size:26px;color:#555}
.rule{position:absolute;top:248px;height:1px;background:#999;width:283px}
.client{position:absolute;width:140px;margin-left:-70px;text-align:center;font-size:15px;font-weight:bold;line-height:1.1}
.footer-nav{position:absolute;left:0;top:1138px;width:784px;height:32px;background:var(--black);text-align:center;font-size:10px;color:#fff;padding-top:11px}
.footer-nav a{color:#fff;text-decoration:none;margin:0 6px}
.copyright{position:absolute;left:0;top:1170px;width:784px;height:30px;background:var(--footer-copy);text-align:center;font-size:9px;color:var(--ink);padding-top:10px}
</style>
</head>
<body>
<div class="page">
  <header class="header">
    <div class="brand"><span class="brand-mark"></span>BRIGHT HARBOR</div>
    <div class="callus">Call Us: <span>02-555-01934</span></div>
  </header>
  <nav class="nav">
    <a style="left:134px">HOME</a>
    <a style="left:231px">PORTFOLIO</a>
    <a style="left:354px">APPROACH AND SERVICES</a>
    <a style="left:547px">NEWS</a>
    <a style="left:642px">CONTACT US</a>
  </nav>
  <section class="hero">
    <svg width="784" height="330" viewBox="0 0 784 330">
      <defs>
        <linearGradient id="bgl" x1="0" y1="0" x2="0" y2="1"><stop offset="0" stop-color="#9a9a9a"/><stop offset=".7" stop-color="#cfcfcf"/><stop offset=".71" stop-color="#e03a40"/><stop offset="1" stop-color="#b5121b"/></linearGradient>
        <linearGradient id="p1" x1="0" y1="0" x2="1" y2="1"><stop offset="0" stop-color="#e8e8e8"/><stop offset=".5" stop-color="#b9a89a"/><stop offset="1" stop-color="#4a4f57"/></linearGradient>
        <linearGradient id="p2" x1="0" y1="0" x2="1" y2="1"><stop offset="0" stop-color="#9fc4e6"/><stop offset=".5" stop-color="#e9d6c4"/><stop offset="1" stop-color="#d9e6f2"/></linearGradient>
      </defs>
      <rect x="0" y="0" width="784" height="310" fill="url(#bgl)"/>
      <polygon points="440,0 464,0 368,316 344,316" fill="#111"/>
      <polygon points="760,0 784,0 690,316 680,316" fill="#111"/>
      <polygon points="28,316 696,316 692,326 24,326" fill="#111"/>
      <polygon points="128,0 440,0 344,316 32,316" fill="url(#p1)" role="img" aria-label="Photo of a smiling businessman in glasses and suit"/>
      <polygon points="464,0 760,0 680,316 368,316" fill="url(#p2)" role="img" aria-label="Photo of a businesswoman holding a pen"/>
    </svg>
  </section>
  <section class="values">
    <div class="value" style="left:79px"><svg viewBox="0 0 36 26" width="36"><rect x="6" y="2" width="24" height="17" rx="2" fill="#333"/><rect x="2" y="20" width="32" height="4" rx="1" fill="#333"/></svg>Innovation</div>
    <div class="value" style="left:211px"><svg viewBox="0 0 36 26" width="36"><g fill="none" stroke="#333" stroke-width="2"><path d="M18 2v20M6 6h24M6 6l-4 10M6 6l4 10M30 6l-4 10M30 6l4 10M12 24h12"/></g><path d="M1 16h10a5 4 0 0 1-10 0zM25 16h10a5 4 0 0 1-10 0z" fill="#333"/></svg>Integrity</div>
    <div class="value" style="left:364px"><svg viewBox="0 0 40 30" width="40"><circle cx="14" cy="17" r="9" fill="none" stroke="#333" stroke-width="6" stroke-dasharray="3 2.5"/><circle cx="30" cy="8" r="5" fill="none" stroke="#333" stroke-width="4" stroke-dasharray="2 1.8"/><circle cx="31" cy="23" r="5" fill="none" stroke="#333" stroke-width="4" stroke-dasharray="2 1.8"/></svg>Knowledgeable</div>
    <div class="value" style="left:514px"><svg viewBox="0 0 34 26" width="34"><path d="M2 2v22h30" fill="none" stroke="#333" stroke-width="3"/><rect x="8" y="10" width="5" height="12" fill="#333"/><rect x="15" y="5" width="5" height="17" fill="#333"/><rect x="22" y="12" width="5" height="10" fill="#333"/></svg>Growth</div>
    <div class="value" style="left:672px"><svg viewBox="0 0 44 26" width="44"><rect x="2" y="10" width="40" height="14" fill="#333"/><g fill="#333"><circle cx="8" cy="5" r="3"/><circle cx="17" cy="5" r="3"/><circle cx="27" cy="5" r="3"/><circle cx="36" cy="5" r="3"/></g><g fill="#f4f4f4"><circle cx="12" cy="14" r="2.5"/><circle cx="22" cy="14" r="2.5"/><circle cx="32" cy="14" r="2.5"/></g></svg>Entrepreneurship</div>
  </section>
  <section class="audiences">
    <div class="audience" style="left:49px">
      <h2>INVESTORS / BUSINESS ANGELS</h2>
      <div class="sub" style="width:280px">looking for better access to investments</div>
      <p>Are you wondering where to invest your money and looking for a successfull ROI? You just came to the right place, we can help you decide and find a good business investment the you desire.</p>
      <div class="cta"><svg width="20" height="18" viewBox="0 0 20 18"><rect x="1" y="6" width="18" height="11" fill="#ccc"/><path d="M1 6l9 6 9-6" fill="none" stroke="#999"/><circle cx="10" cy="5" r="4" fill="#bbb"/></svg><span>contact us and get a business proposal or<br>submit invsestment proposal</span></div>
    </div>
    <div class="audience" style="left:424px">
      <h2>ENTREPRENEURS AND STARTUPS</h2>
      <div class="sub" style="width:292px">looking for investors</div>
      <p>Have a business in mind but don't have enought funds to continue with the venture? This is the right place to take your business into a higher next and look for investors to help you achive the business of your dreams.</p>
      <div class="cta"><svg width="20" height="18" viewBox="0 0 20 18"><rect x="1" y="6" width="18" height="11" fill="#ccc"/><path d="M1 6l9 6 9-6" fill="none" stroke="#999"/><circle cx="10" cy="5" r="4" fill="#bbb"/></svg><span>contact us and submit your business proposal</span></div>
    </div>
    <div class="rule" style="left:53px"></div>
    <div class="portfolio-title">PORTFOLIO</div>
    <div class="rule" style="left:453px"></div>

    <div class="client" style="left:108px;top:305px;color:#8c1a22">Velora Group</div>
    <div class="client" style="left:248px;top:305px;color:#3a8c2a">Fizzmart</div>
    <div class="client" style="left:376px;top:305px;color:#2a4a8c">Quarto Consulting</div>
    <div class="client" style="left:544px;top:305px;color:#7a1020">Solvenne</div>
    <div class="client" style="left:676px;top:305px;color:#1b2f8c">Harbour Reed Festival</div>

    <div class="client" style="left:108px;top:378px;color:#c0121c">Nibbla</div>
    <div class="client" style="left:248px;top:378px;color:#333">Verdana Day Spa</div>
    <div class="client" style="left:376px;top:378px;color:#c89a2a">Ostro</div>
    <div class="client" style="left:544px;top:378px;color:#7a1020">Lumio</div>
    <div class="client" style="left:676px;top:378px;color:#2a4ac0">Canvas Keep</div>

    <div class="client" style="left:108px;top:452px;color:#555">Hale &amp; Orwin</div>
    <div class="client" style="left:248px;top:452px;color:#2a5a9c">Autoscout Solutions</div>
    <div class="client" style="left:376px;top:452px;color:#b8a020">Petal Crate</div>
    <div class="client" style="left:544px;top:452px;color:#2a4a9c">Meridian Care Recruitment</div>
    <div class="client" style="left:676px;top:452px;color:#1b3a8c">Keystone Super</div>

    <div class="client" style="left:108px;top:524px;color:#1a6ac0">Ember Relief Trust</div>
    <div class="client" style="left:248px;top:524px;color:#222">Shearline Salons</div>
    <div class="client" style="left:376px;top:524px;color:#2a6a4a">Tamsin International</div>
  </section>
  <footer>
    <div class="footer-nav"><a>HOME</a>·<a>PORTFOLIO</a>·<a>APPROACH AND SERVICES</a>·<a>NEWS</a>·<a>CONTACT US</a></div>
    <div class="copyright">© Copyright 2013 BRIGHT HARBOR All Rights Reserved.</div>
  </footer>
</div>
</body>
</html>
```